Redesign one screen in a mobile app

I have an app called Toasts and Tallies (available on iOS and Android). This app allows wedding guests to bet on things that happen during a wedding they are attending (think: will the groom cry when the bride walks down the aisle...). The event is set up by someone called the "event leader", typically this is the bride or the groom.

Once event details, bets, and $ values of the bets are entered, the event leader publishes the event and gets to the event detail homescreen, where they can manage their event. The three main things they can do are:

1.) Share the event with other guests to join in the betting.
2.) Edit the event -- add, change, or delete bets.
3.) Add a co-organizer. If you are the bride or the groom, you want someone else managing the event on your wedding day.

I'd like to redesign this page, make it simpler, and *focus attention on sharing the event.* The biggest goal of this page is getting event leaders to share the event. We want them to invite as many wedding guests as possible.

To that end, I would like to also introducing "sharing tiers" to entice more sharing and I'd like this to be something event leaders can easily see once they hit the event homescreen. Tiers are as follows:
Share with 1 guest, unlock co-organizer feature.
Share with 5 guests, unlock physical placard with custom QR code.
Share with 10 guests, we split our proceeds with the bride and groom.
Share with 20 guests, you are entered into $250 monthly raffle.

Some additional requests:
+ Please do not use current fonts. We want new fonts that are cleaner.
+ Share options should stay the same (copy, share, QR code)
+ Need to keep "help" question mark on page as well.
+ Maintain colors generally. Red button color must be kept as is because it's used throughout app. Slight variations to other colors OK.
+ Navigation at bottom must remain.
+ Feel free to add moving elements as well, like gifs.
+ Final design delivered in Figma.
Updates

Submissions need to be app designs. Not webpages.

The current actions shown on the page need to remain - share event, edit event, add a Co-Organizer. But the goal of the design is to make the page simpler, not more complicated.

Sharing tiers can be a separate screen, linked from the event home screen. This information does not need to live on the same page!

Target Market(s)

25-40 year olds

Industry/Entity Type

Mobile Apps - Betting

Font styles to use
Sans Serif
Other font styles liked:
• I like poppins, but open to other options.

Requirements
Must have
• Fun design that focuses on sharing an event. Design delievered in Figma.

```html
<!DOCTYPE html>
<html lang="en">
<head>
<meta charset="utf-8">
<title>Toasts and Tallies – Sharing tiers</title>
<link href="https://fonts.googleapis.com/css2?family=Poppins:wght@400;500&display=swap" rel="stylesheet">
<style>
  :root {
    --bg: #f3f4f9;
    --surface: #ffffff;
    --brand-red: #e26355;
    --brand-red-deep: #b9473c;
    --check-soft: #f2b1a8;
    --ink: #111111;
    --field: #f3f4f9;
  }
  * { box-sizing: border-box; margin: 0; padding: 0; }
  html, body {
    width: 1200px; height: 2601px; overflow: hidden;
    background: var(--bg);
    font-family: "Poppins", sans-serif;
    color: var(--ink);
  }
  .screen {
    position: absolute; left: 0; top: 0;
    width: 430px; height: 932px;
    transform: scale(2.7907); transform-origin: 0 0;
    background: var(--bg);
  }
  .icon-button {
    position: absolute; width: 55px; height: 55px; border-radius: 50%;
    background: var(--surface); display: flex; align-items: center; justify-content: center;
  }
  .icon-button--back { left: 21px; top: 36px; }
  .icon-button--help { left: 354px; top: 36px; }
  .section-title { position: absolute; font-size: 22px; font-weight: 400; line-height: 1; }
  .section-title--tiers { left: 31px; top: 130px; }
  .section-title--share { left: 21px; top: 461px; }
  .card { position: absolute; background: var(--surface); border-radius: 22px; }
  .card--tiers { left: 21px; top: 163px; width: 388px; height: 292px; }
  .card--share { left: 21px; top: 496px; width: 388px; height: 204px; }
  .card-heading { position: absolute; left: 27px; top: 21px; font-size: 18px; font-weight: 400; }
  .tier { position: absolute; left: 20px; width: 360px; height: 50px; }
  .tier-badge {
    position: absolute; left: 0; top: 0; width: 152px; height: 50px;
    border-radius: 12px; background: var(--brand-red);
  }
  .tier-check {
    position: absolute; left: 12px; top: 12px; width: 26px; height: 26px; border-radius: 50%;
    background: var(--brand-red-deep); display: flex; align-items: center; justify-content: center;
  }
  .tier-check--done { background: var(--surface); }
  .tier-count {
    position: absolute; right: 16px; top: 0; line-height: 50px;
    color: #fff; font-size: 19px; font-weight: 400;
  }
  .tier-reward {
    position: absolute; left: 168px; top: 50%; transform: translateY(-50%);
    font-size: 12.5px; font-weight: 500; line-height: 1.25;
  }
  .share-note {
    position: absolute; left: 22px; top: 22px; width: 350px;
    font-size: 12.5px; line-height: 20px; font-weight: 400;
  }
  .share-link { position: absolute; left: 19px; top: 74px; width: 350px; height: 38px; border-radius: 12px; background: var(--field); }
  .share-action {
    position: absolute; top: 132px; width: 109px; height: 49px; border-radius: 14px;
    background: var(--brand-red); color: #fff; font-size: 14px; font-weight: 400;
    display: flex; align-items: center; justify-content: center; gap: 6px;
  }
  .share-action--copy { left: 22px; }
  .share-action--share { left: 140px; }
  .share-action--qr { left: 258px; }
</style>
</head>
<body>
<main class="screen">
  <div class="icon-button icon-button--back" aria-label="Back">
    <svg width="32" height="22" viewBox="0 0 32 22" fill="none" stroke="#111" stroke-width="2.2" stroke-linecap="round" stroke-linejoin="round"><path d="M30 11H2M11 2 2 11l9 9"/></svg>
  </div>
  <div class="icon-button icon-button--help" aria-label="Help">
    <svg width="34" height="34" viewBox="0 0 34 34" fill="none" stroke="#222" stroke-width="2" stroke-linecap="round"><circle cx="17" cy="17" r="15.5"/><path d="M12.5 13a4.6 4.6 0 0 1 9 1.2c0 3-4.5 3.6-4.5 6.6"/><circle cx="17" cy="25" r="0.6" fill="#222"/></svg>
  </div>

  <h1 class="section-title section-title--tiers">Sharing tiers</h1>
  <section class="card card--tiers">
    <h2 class="card-heading">Share to unlock</h2>

    <div class="tier" style="top:54px">
      <div class="tier-badge">
        <span class="tier-check tier-check--done"><svg width="14" height="11" viewBox="0 0 14 11" fill="none" stroke="#e26355" stroke-width="2" stroke-linecap="round" stroke-linejoin="round"><path d="M1.5 5.5 5.2 9 12.5 1.8"/></svg></span>
        <span class="tier-count">1 Guest</span>
      </div>
      <p class="tier-reward">Unlock co-organizer feature</p>
    </div>

    <div class="tier" style="top:109px">
      <div class="tier-badge">
        <span class="tier-check"><svg width="12" height="9" viewBox="0 0 14 11" fill="none" stroke="#f2b1a8" stroke-width="2" stroke-linecap="round" stroke-linejoin="round"><path d="M1.5 5.5 5.2 9 12.5 1.8"/></svg></span>
        <span class="tier-count">5 Guest</span>
      </div>
      <p class="tier-reward">Unlock physical placard<br>with custom QR code</p>
    </div>

    <div class="tier" style="top:164px">
      <div class="tier-badge">
        <span class="tier-check"><svg width="12" height="9" viewBox="0 0 14 11" fill="none" stroke="#f2b1a8" stroke-width="2" stroke-linecap="round" stroke-linejoin="round"><path d="M1.5 5.5 5.2 9 12.5 1.8"/></svg></span>
        <span class="tier-count">10 Guest</span>
      </div>
      <p class="tier-reward">We split our proceeds with<br>the bride and groom</p>
    </div>

    <div class="tier" style="top:219px">
      <div class="tier-badge">
        <span class="tier-check"><svg width="12" height="9" viewBox="0 0 14 11" fill="none" stroke="#f2b1a8" stroke-width="2" stroke-linecap="round" stroke-linejoin="round"><path d="M1.5 5.5 5.2 9 12.5 1.8"/></svg></span>
        <span class="tier-count">20 Guest</span>
      </div>
      <p class="tier-reward">You are entered into<br>$250 monthly raffle</p>
    </div>
  </section>

  <h1 class="section-title section-title--share">Share Event</h1>
  <section class="card card--share">
    <p class="share-note">Inviting guests to join by sharing the event below,<br>Each&nbsp; guest pays $2.99 to join</p>
    <div class="share-link"></div>
    <div class="share-action share-action--copy">
      <svg width="20" height="20" viewBox="0 0 24 24" fill="none" stroke="#fff" stroke-width="2.2" stroke-linecap="round"><path d="M10 14a4.5 4.5 0 0 0 6.4 0l3.3-3.3a4.5 4.5 0 0 0-6.4-6.4L11.8 5.8"/><path d="M14 10a4.5 4.5 0 0 0-6.4 0l-3.3 3.3a4.5 4.5 0 0 0 6.4 6.4l1.5-1.5"/></svg>
      <span>Copy</span>
    </div>
    <div class="share-action share-action--share">
      <svg width="19" height="19" viewBox="0 0 24 24" fill="#fff" stroke="#fff" stroke-width="2"><circle cx="18" cy="5" r="3"/><circle cx="6" cy="12" r="3"/><circle cx="18" cy="19" r="3"/><path d="M8.6 10.5 15.4 6.5M8.6 13.5l6.8 4" fill="none"/></svg>
      <span>Share</span>
    </div>
    <div class="share-action share-action--qr">
      <svg width="22" height="22" viewBox="0 0 24 24" fill="none" stroke="#fff" stroke-width="2" stroke-linejoin="round"><rect x="2.5" y="2.5" width="7.5" height="7.5" rx="2"/><rect x="14" y="2.5" width="7.5" height="7.5" rx="2"/><rect x="2.5" y="14" width="7.5" height="7.5" rx="2"/><path d="M14 14h3v3h-3zM18.5 18.5h3v3h-3zM14 20v1.5M21.5 14v2"/></svg>
      <span>QR code</span>
    </div>
  </section>
</main>
</body>
</html>
```